Bright Harbor Advisors, LLC Business Card Design

Website URL: www.brightharboradvisors.example
I have attached a previous design that I find "okay" and adequate, but I wanted to explore some more distinctive/creative professional versions.
Our company provides business owners, executives and managers valuable information to help them make better people decisions. Our primary means of providing this information is through a comprehensive suite of employee assessment products across the employee life cycle that help clients better select, manage and retain talent. Company tagline is: Measure Talent, Forecast Success. Our employee assessment products fall into the following 3 categories:
- Assessments for Hiring Talent
- Assessments for Developing Talent
- Assessments for Retaining Talent
Please view our 3 minute overview video (link below) to get a sense of who we are:
http://videohost.example/Qx83LmTz2wa
Our business personality is competent, modern, & friendly...driven by developing long lasting client relationships as opposed to one time customer transactions. We would like to see designs that are professional yet distinctive "cool business card!" and use primary logo colors/complementary color . Not sure if I prefer the gray font as shown in previous design or black...open to suggestions.
The final design should communicate competence, trust, and solutions. Also, I am an authorized business partner and consultant with two organizations that provide the assessment products I will market/use with clients. Attached are files for Vantora Associates and Lindqvist Partners that should be incorporated into the design (*very small but readable)

Industry/Entity Type
Business
Contact Information for Business Card
Howard Ellery
Founder and Managing Partner
4518 North Tallow Creek Road
Suite 410
Atlanta GA 30318-4417
Office: 678.555.0142
hellery@brightharboradvisors.example
www.brightharbraadvisors.example

```html
<!DOCTYPE html>
<html lang="en">
<head>
<meta charset="utf-8">
<title>Bright Harbor Advisors – Business Card</title>
<link rel="stylesheet" href="https://fonts.googleapis.com/css2?family=Source+Sans+3:ital,wght@0,400;0,600;0,700;1,400;1,600&display=swap">
<style>
  :root {
    --backdrop: #e9e6e1;
    --card: #f5ede1;
    --navy: #2b2a6b;
    --blue: #1b7fcf;
    --badge-a: #8c8a92;
    --badge-b: #b8653a;
  }
  * { margin: 0; padding: 0; box-sizing: border-box; }
  html, body {
    width: 1200px; height: 956px; overflow: hidden;
    background: var(--backdrop);
    font-family: "Source Sans 3", sans-serif;
  }
  .card {
    position: absolute; left: 352px; top: 43px;
    width: 496px; height: 870px;
    background: var(--card);
    box-shadow: 0 4px 18px rgba(0,0,0,.18);
    color: var(--navy);
    text-align: center;
  }
  .brand { position: absolute; top: 82px; left: 0; right: 0; }
  .brand-mark {
    width: 112px; height: 112px; border-radius: 50%;
    background: var(--blue); margin: 0 auto 22px;
  }
  .brand-name {
    font-size: 44px; font-weight: 700; color: var(--navy);
    line-height: 1; letter-spacing: -.5px;
  }
  .tagline {
    margin-top: 16px; font-size: 21px; color: var(--blue); letter-spacing: .4px;
  }
  .tagline .dot { font-size: 16px; vertical-align: 2px; padding: 0 4px; }
  .person { position: absolute; top: 392px; left: 0; right: 0; }
  .person-name { font-size: 29px; font-weight: 700; color: var(--blue); letter-spacing: .3px; }
  .person-title { font-size: 22px; font-style: italic; margin-top: 2px; }
  .contact {
    position: absolute; top: 502px; left: 48px; right: 20px;
    text-align: left; font-size: 22px; line-height: 29px; list-style: none;
  }
  .contact li { display: flex; align-items: flex-start; }
  .contact svg { width: 18px; height: 20px; margin: 5px 6px 0 0; flex: none; fill: var(--blue); }
  .contact .indent { padding-left: 24px; }
  .website {
    position: absolute; top: 658px; left: 0; right: 0;
    font-size: 24px; font-style: italic; color: var(--blue);
  }
  .partners {
    position: absolute; bottom: 40px; left: 54px; right: 54px;
    display: flex; justify-content: space-between; align-items: center;
  }
  .partner-badge { display: block; }
</style>
</head>
<body>
  <main class="card">
    <header class="brand">
      <div class="brand-mark"></div>
      <div class="brand-name">Bright Harbor Advisors</div>
      <p class="tagline">Measure Talent <span class="dot">●</span> Forecast Success</p>
    </header>

    <section class="person">
      <h1 class="person-name">HOWARD ELLERY</h1>
      <p class="person-title">Founder &amp; Managing Partner</p>
    </section>

    <ul class="contact">
      <li>
        <svg viewBox="0 0 18 20"><path d="M9 0a7 7 0 0 0-7 7c0 5 7 13 7 13s7-8 7-13a7 7 0 0 0-7-7zm0 10a3 3 0 1 1 0-6 3 3 0 0 1 0 6z"/></svg>
        <span>4518 North Tallow Creek Rd, Ste 410</span>
      </li>
      <li class="indent">Atlanta GA 30318-4417</li>
      <li>
        <svg viewBox="0 0 18 20"><path d="M4 2l3 0 2 5-2 2c1 2 3 4 5 5l2-2 5 2v3c0 1-1 2-2 2C8 19 1 12 1 4c0-1 1-2 3-2z" transform="scale(.85) translate(1 1)"/></svg>
        <span>678.555.0142</span>
      </li>
      <li>
        <svg viewBox="0 0 18 20"><path d="M1 6h16v10H1z"/><path d="M1 6l8 6 8-6" fill="none" stroke="#f5ede1" stroke-width="1.5"/></svg>
        <span>hellery@brightharboradvisors.example</span>
      </li>
    </ul>

    <p class="website">www.brightharbraadvisors.example</p>

    <footer class="partners">
      <svg class="partner-badge" width="150" height="34" viewBox="0 0 150 34" role="img" aria-label="Vantora Associates authorized partner badge">
        <rect x="0" y="4" width="150" height="26" rx="3" fill="var(--badge-a)" opacity=".55"/>
      </svg>
      <svg class="partner-badge" width="130" height="40" viewBox="0 0 130 40" role="img" aria-label="Lindqvist Partners certified consultant badge">
        <rect x="0" y="4" width="130" height="32" rx="3" fill="var(--badge-b)" opacity=".5"/>
      </svg>
    </footer>
  </main>
</body>
</html>
```